Business Cards for Branding (Advertising) Agency

We need stylish and cool business cards.
Additional info:
1) Logo - see the attachment. You can use either the three penguins or just one penguin face (square or round) - at your discretion.
2) Text and other stuff for business card:
front side:
-Logo and company name: company name - Northern Herons - should be in English as is in logo. This is the only exception. The rest of the text will be in Russian.
-Who we are: Брендинговое агентство
-First and last name:
-Position: Управляющий партнёр
-Address:
-Phone:
-Email:
-Website:
Note: please don't use names of information fields, such as: who we are, first and last name, position, address, phone, email and website.

3) Our suggestions on design:
-The backside of the business card can be either blank or has something on it - at your discretion.
-The business card background should be either white or grey (you can use any tone of grey).

Additional Information:
1) БРЕНДИНГОВОЕ АГЕНТСТВО
2) ул. Верескова - these two words should be together on the same line
3) тел.: +7 (495) 381-60-92
моб.: +7 (916) 507-28-14

Reason: We would like to receive more stylish designs.

```html
<!DOCTYPE html>
<html lang="ru">
<head>
<meta charset="utf-8">
<title>Northern Herons — визитные карточки</title>
<link rel="stylesheet" href="https://fonts.googleapis.com/css2?family=PT+Sans:wght@400;700&display=swap">
<style>
  :root {
    --page-bg: #5a5a5c;
    --card-dark: #1d1d1e;
    --card-dark-2: #262627;
    --card-light: #ffffff;
    --ink-dark: #111111;
    --ink-grey: #8a8a8a;
    --ink-light: #f2f2f2;
    --ink-muted: #bdbdbd;
    --art-tone-1: #d9d9d9;
    --art-tone-2: #9a9a9a;
  }
  * { box-sizing: border-box; margin: 0; padding: 0; }
  html, body {
    width: 1200px; height: 1023px; overflow: hidden;
    background: var(--page-bg);
    font-family: "PT Sans", Arial, sans-serif;
  }
  .sheet { position: relative; width: 1200px; height: 1023px; }
  .card {
    position: absolute; left: 220px; width: 760px; height: 434px;
    border-radius: 14px; overflow: hidden;
    box-shadow: 0 14px 30px rgba(0,0,0,.35);
  }
  .card--front { top: 58px; background: var(--card-dark); }
  .card--back  { top: 531px; background: linear-gradient(160deg, var(--card-dark-2), var(--card-dark)); }

  /* front */
  .front__header {
    position: absolute; left: 0; top: 0; width: 100%; height: 178px;
    background: var(--card-light);
  }
  .front__mascots {
    position: absolute; left: 24px; top: 44px; width: 200px; height: 150px;
    border-radius: 60px 60px 20px 20px;
    background: linear-gradient(180deg, var(--art-tone-1), var(--art-tone-2));
  }
  .front__brand {
    position: absolute; left: 248px; top: 48px;
    font-weight: 700; font-size: 46px; letter-spacing: 3px;
    color: var(--ink-dark); text-transform: uppercase; line-height: 1;
    white-space: nowrap;
  }
  .front__tagline {
    position: absolute; left: 250px; top: 116px;
    font-size: 31px; letter-spacing: 1px; color: var(--ink-grey);
    text-transform: uppercase; line-height: 1; white-space: nowrap;
  }
  .contacts {
    position: absolute; left: 40px; top: 210px; list-style: none;
    color: var(--ink-light); font-size: 19px; line-height: 1.2;
  }
  .contacts li { display: flex; align-items: flex-start; gap: 14px; margin-bottom: 7px; }
  .contacts svg { width: 18px; height: 18px; flex: none; margin-top: 3px; fill: var(--ink-muted); }
  .contacts__label { color: var(--ink-muted); }
  .person { position: absolute; right: 40px; top: 214px; text-align: right; }
  .person__name {
    font-weight: 700; font-size: 30px; color: var(--ink-light);
    text-transform: uppercase; letter-spacing: 1px;
  }
  .person__role { font-weight: 700; font-size: 26px; color: var(--ink-muted); }

  /* back */
  .back__mascots {
    position: absolute; left: 250px; top: 42px; width: 260px; height: 130px;
    border-radius: 65px 65px 24px 24px;
    background: linear-gradient(180deg, var(--art-tone-1), var(--art-tone-2));
  }
  .back__brand {
    position: absolute; left: 0; width: 100%; top: 196px; text-align: center;
    font-weight: 700; font-size: 76px; letter-spacing: 4px; line-height: 1;
    color: var(--ink-light); text-transform: uppercase;
  }
  .social {
    position: absolute; left: 34px; bottom: 28px;
    display: flex; align-items: center; gap: 10px;
    font-size: 22px; color: var(--ink-light);
  }
  .social__mark { width: 22px; height: 22px; background: var(--ink-muted); border-radius: 4px; }
</style>
</head>
<body>
<main class="sheet">

  <section class="card card--front" aria-label="Лицевая сторона визитки">
    <header class="front__header">
      <div class="front__brand">Northern Herons</div>
      <div class="front__tagline">Брендинговое агентство</div>
    </header>
    <div class="front__mascots" role="img" aria-label="Иллюстрация: три фирменных персонажа агентства"></div>

    <ul class="contacts">
      <li>
        <svg viewBox="0 0 24 24" aria-hidden="true"><path d="M6.6 10.8a15.2 15.2 0 0 0 6.6 6.6l2.2-2.2c.3-.3.7-.4 1-.2 1.1.4 2.3.6 3.6.6.6 0 1 .4 1 1V20c0 .6-.4 1-1 1C10.6 21 3 13.4 3 4c0-.6.4-1 1-1h3.5c.6 0 1 .4 1 1 0 1.3.2 2.5.6 3.6.1.3 0 .7-.2 1z"/></svg>
        <span><span class="contacts__label">тел.:</span> +7 (495) 381-60-92<br><span class="contacts__label">моб.:</span> +7 (916) 507-28-14</span>
      </li>
      <li>
        <svg viewBox="0 0 24 24" aria-hidden="true"><path d="M2 5h20v14H2zM4 7v.4l8 5.2 8-5.2V7z"/></svg>
        <span>maria@northernherons.ru</span>
      </li>
      <li>
        <svg viewBox="0 0 24 24" aria-hidden="true"><path d="M10 14a4 4 0 0 1 0-5.7l3-3a4 4 0 0 1 5.7 5.7l-1.4 1.4-1.4-1.4 1.4-1.4a2 2 0 0 0-2.9-2.9l-3 3a2 2 0 0 0 0 2.9zm4-4a4 4 0 0 1 0 5.7l-3 3A4 4 0 0 1 5.3 13l1.4-1.4 1.4 1.4-1.4 1.4a2 2 0 0 0 2.9 2.9l3-3a2 2 0 0 0 0-2.9z"/></svg>
        <span>www.northernherons.ru</span>
      </li>
      <li>
        <svg viewBox="0 0 24 24" aria-hidden="true"><path d="M12 2a7 7 0 0 0-7 7c0 5.2 7 13 7 13s7-7.8 7-13a7 7 0 0 0-7-7zm0 9.5A2.5 2.5 0 1 1 12 6.5a2.5 2.5 0 0 1 0 5z"/></svg>
        <span>117302, г. Москва,<br>ул. Верескова, д.18, стр.2</span>
      </li>
    </ul>

    <div class="person">
      <div class="person__name">Мария Ковалёва</div>
      <div class="person__role">Управляющий партнёр</div>
    </div>
  </section>

  <section class="card card--back" aria-label="Оборотная сторона визитки">
    <div class="back__mascots" role="img" aria-label="Иллюстрация: три фирменных персонажа агентства"></div>
    <div class="back__brand">Northern<br>Herons</div>
    <div class="social">
      <span class="social__mark" aria-hidden="true"></span>
      <span>NorthernHerons</span>
    </div>
  </section>

</main>
</body>
</html>
```